CRPG is needing business cards, and stationary created.

Pixel Forge created a logo for our business, and now we are wanting business cards, and stationary. I have included two designs of the same logo. Please feel free to use them as you want. The name of the company is Cedar Ridge Property Group LLC, the address is 812 NE Willow Ln., Suite 9, the city & state is Bend, Oregon, zip code is 97815, Telephone number is 541-327-4489, Fax number is 541-327-6051, the name on the business card is Carl Whitby CMCA

Industry/Entity Type

Property Management

Contact Information for Business Card

The card needs to look professional. Upscale.

Requirements
Must have
• The colors we are using are on the logo that has been uploaded.

```html
<!DOCTYPE html>
<html lang="en">
<head>
<meta charset="utf-8">
<title>Cedar Ridge Property Group — Business Card</title>
<link rel="stylesheet" href="https://fonts.googleapis.com/css2?family=Open+Sans:wght@400;600;700&display=swap">
<style>
  :root {
    --backdrop: #2b2c2e;
    --slate: #3e4a5c;
    --slate-light: #56627a;
    --green: #1a8c78;
    --paper: #ffffff;
    --ink: #4f5356;
  }
  * { margin: 0; padding: 0; box-sizing: border-box; }
  html, body {
    width: 1200px; height: 892px; overflow: hidden;
    background: var(--backdrop);
    font-family: "Open Sans", Arial, sans-serif;
  }
  .canvas { position: relative; width: 1200px; height: 892px; }
  .card {
    position: absolute; width: 540px; height: 309px;
    overflow: hidden; border-radius: 2px;
    box-shadow: 0 14px 30px rgba(0,0,0,.45);
  }
  .card-back {
    left: 50px; top: 100px;
    background: linear-gradient(160deg, var(--slate-light) 0%, var(--slate) 70%, #374252 100%);
    color: var(--paper);
  }
  .back-mark {
    position: absolute; left: 0; right: 0; top: 92px;
    text-align: center;
    font-weight: 700; font-size: 64px; letter-spacing: 4px;
    color: var(--paper);
  }
  .back-web {
    position: absolute; left: 0; right: 0; bottom: 48px;
    text-align: center;
    font-size: 13px; letter-spacing: 2.6px;
  }
  .card-front { left: 610px; top: 470px; background: var(--paper); color: var(--ink); }
  .bands { position: absolute; inset: 0; }
  .brand {
    position: absolute; left: 24px; top: 92px;
    display: flex; align-items: center; gap: 10px;
  }
  .brand-square { width: 28px; height: 28px; background: var(--slate); }
  .brand-name {
    font-weight: 700; font-size: 24px; letter-spacing: .5px;
    color: var(--green);
  }
  .holder-name {
    position: absolute; left: 24px; top: 158px;
    font-weight: 700; font-size: 19px; color: var(--paper);
  }
  .address {
    position: absolute; right: 26px; top: 172px;
    text-align: right; font-size: 12.5px; line-height: 1.4;
  }
  .contact {
    position: absolute; left: 24px; bottom: 22px;
    list-style: none; font-size: 13.5px; line-height: 1.45;
  }
  .contact li { display: flex; align-items: center; gap: 7px; }
  .contact svg { width: 13px; height: 13px; fill: var(--green); }
</style>
</head>
<body>
<main class="canvas">
  <section class="card card-back">
    <div class="back-mark">CRPG</div>
    <div class="back-web">www.cedarridgepropertygroup.com</div>
  </section>

  <section class="card card-front">
    <svg class="bands" viewBox="0 0 540 309" aria-hidden="true">
      <polygon points="332,124 540,124 540,152 320,152" fill="var(--slate)"/>
      <polygon points="0,152 320,152 306,192 0,192" fill="var(--green)"/>
    </svg>

    <div class="brand">
      <span class="brand-square"></span>
      <span class="brand-name">CEDAR RIDGE</span>
    </div>

    <div class="holder-name">Carl Whitby CMCA</div>

    <address class="address" style="font-style:normal">
      812 NE Willow Ln., Suite 9<br>
      Bend, Oregon 97815
    </address>

    <ul class="contact">
      <li>
        <svg viewBox="0 0 16 16" aria-label="Telephone"><path d="M2 5c0-2 3-3 6-3s6 1 6 3v1h-3V5H5v1H2zM4 7h8l2 6H2z"/></svg>
        541-327-4489
      </li>
      <li>
        <svg viewBox="0 0 16 16" aria-label="Fax"><path d="M4 1h8v5H4zM1 7h14v7H1zM4 10h8v3H4z"/></svg>
        541-327-6051
      </li>
    </ul>
  </section>
</main>
</body>
</html>
```